Retail Package for Ammunition Company

We are looking for a packaging design for a retail boxed ammunition. The "look". Attached will be the logo to be used. The logo is attached and a can be manipulated on the box. Box to represent strength and accuracy. Will need to provide .psd files to allow in house personnel to add/remove text to other calibers and warnings. Wow me with your designs!

Browse Other Brands: http://www.brightfalconstore.com/brands

The packaging needs to include:
Logo- provided and the following text:

FRONT 1. 9mm 115gr FMJ

BACK 2. WARNING: To avoid serious injury: (1) use only ammunition in good condition; use only in modern firearms in good condition marked for .22 Long Rifle (LR) cartridges; (2) always be sure barrel is free of any obstructions; the barrel should be checked in case of light recoil, or an unusually loud or weak sound heard during firing; (3) wear eye and ear protection; (4) if gun fails to fire, avoid exposure to breech when unloading and point muzzle in a safe direction. Keep firearm pointed in safe direction at all times; (5) discharge may occur if rim is struck; handle with caution, do not drop. (6) Do not shoot at hard surfaces or water to prevent ricochet; (7) Bullet is capable of traveling extreme distances. Know your backstop; (8) Store in cool dry place

3. LEAD WARNING: Discharging firearms in poorly ventilated areas, cleaning firearms, or handling ammunition may result in exposure to lead and other substances known to cause birth defects, reproductive harm, and other serious physical injury. Have adequate ventilation at all times. Wash hands thoroughly after exposure.

Dimensions ; (LxWxH): 5.25" x 2.625" x 1.125"

Target Market(s)

Ammunition Industry

```html
<!DOCTYPE html>
<html lang="en">
<head>
<meta charset="utf-8">
<title>Iron Ridge Armory – 9mm Retail Box Dieline</title>
<link rel="stylesheet" href="https://fonts.googleapis.com/css2?family=Black+Ops+One&family=Roboto+Slab:wght@700&family=Roboto:wght@400;700&display=swap">
<style>
  :root {
    --paper: #ffffff;
    --wood-light: #8a6a4c;
    --wood-mid: #6e5038;
    --wood-dark: #4a3322;
    --frame-edge: #3a2718;
    --brand-red: #7a1a14;
    --stencil: #2a1a10;
    --alert-red: #d9261c;
    --ink: #1e1e1e;
  }
  * { box-sizing: border-box; margin: 0; padding: 0; }
  html, body { width: 795px; height: 1200px; overflow: hidden; background: var(--paper); }
  .canvas { position: relative; width: 795px; height: 1200px; }

  .panel {
    position: absolute;
    background: linear-gradient(180deg, var(--wood-light), var(--wood-mid) 55%, var(--wood-dark));
    border: 1px solid var(--frame-edge);
  }
  .panel-inset {
    position: absolute;
    overflow: hidden;
    background: linear-gradient(180deg, var(--wood-mid), var(--wood-light) 50%, var(--wood-mid));
    box-shadow: inset 0 0 8px rgba(0,0,0,.65);
    display: flex; align-items: center; justify-content: center;
  }

  .back { left: 160px; top: 61px; width: 479px; height: 221px; border-radius: 4px 4px 0 0; }
  .top-side { left: 160px; top: 282px; width: 479px; height: 113px; }
  .front { left: 160px; top: 395px; width: 479px; height: 237px; }
  .bottom-side { left: 160px; top: 632px; width: 479px; height: 107px; border-radius: 0 0 4px 4px; }
  .end-flap { top: 391px; width: 110px; height: 248px; border-radius: 4px; }
  .end-left { left: 60px; }
  .end-right { left: 629px; }

  .warning-sheet {
    position: absolute; left: 46px; top: 43px; width: 379px; height: 166px;
    background: var(--paper);
    transform: rotate(180deg);
    padding: 8px 10px;
    font-family: "Roboto", sans-serif; color: var(--ink);
    overflow: hidden;
  }
  .warning-title {
    display: inline-block; background: var(--alert-red); color: #fff;
    font-weight: 700; font-size: 10px; padding: 2px 6px; letter-spacing: .3px;
  }
  .warning-body { font-size: 6.2px; line-height: 1.55; margin: 4px 0 6px; }

  .brand-name {
    font-family: "Roboto Slab", serif; font-weight: 700;
    color: var(--brand-red); letter-spacing: 1px; white-space: nowrap;
  }
  .brand-mark { display: inline-block; width: 12px; height: 12px; border-radius: 50%; background: var(--brand-red); margin-right: 8px; vertical-align: middle; }
  .top-side .brand-lockup { transform: rotate(180deg); font-size: 20px; }
  .bottom-side .brand-lockup { font-size: 20px; }
  .end-lockup {
    text-align: center; font-size: 17px; line-height: 1.15; letter-spacing: .5px;
  }
  .end-left .end-lockup { transform: rotate(90deg); }
  .end-right .end-lockup { transform: rotate(-90deg); }

  .front-brand {
    position: absolute; left: 46px; top: 42px; width: 192px; height: 156px;
    display: flex; align-items: center; justify-content: center; text-align: center;
    font-size: 30px; line-height: 1.1;
  }
  .caliber {
    position: absolute; left: 249px; top: 60px;
    font-family: "Black Ops One", sans-serif; color: var(--stencil);
    font-size: 72px; line-height: 1; letter-spacing: 2px;
  }
  .load {
    position: absolute; left: 249px; top: 145px;
    font-family: "Black Ops One", sans-serif; color: var(--stencil);
    font-size: 28px; line-height: 1; letter-spacing: 2px;
  }
  .wood-grain { position: absolute; inset: 0; }
</style>
</head>
<body>
<main class="canvas">

  <section class="panel back">
    <div class="wood-grain" role="img" aria-label="Weathered wooden crate planks with iron corner rivets"></div>
    <div class="warning-sheet">
      <span class="warning-title">WARNING: To avoid serious injury:</span>
      <p class="warning-body">• use only ammunition in good condition; use only in modern firearms in good condition marked for .22 Long Rifle (LR) cartridges; • always be sure barrel is free of any obstructions; the barrel should be checked in case of light recoil, or an unusually loud or weak sound heard during firing; • wear eye and ear protection; • if gun fails to fire, avoid exposure to breech when unloading and point muzzle in a safe direction. Keep firearm pointed in safe direction at all times; • discharge may occur if rim is struck; handle with caution, do not drop. • Do not shoot at hard surfaces or water to prevent ricochet; • Bullet is capable of traveling extreme distances. Know your backstop; • Store in cool dry place</p>
      <span class="warning-title">LEAD WARNING:</span>
      <p class="warning-body">Discharging firearms in poorly ventilated areas, cleaning firearms, or handling ammunition may result in exposure to lead and other substances known to cause birth defects, reproductive harm, and other serious physical injury. Have adequate ventilation at all times. Wash hands thoroughly after exposure.</p>
    </div>
  </section>

  <section class="panel top-side">
    <div class="panel-inset" style="left:30px;top:40px;width:419px;height:55px;">
      <div class="brand-name brand-lockup"><span class="brand-mark"></span>IRON RIDGE ARMORY</div>
    </div>
  </section>

  <section class="panel front">
    <div class="panel-inset" style="left:30px;top:28px;width:419px;height:185px;" role="img" aria-label="Wooden crate planks with scattered bullet holes"></div>
    <div class="brand-name front-brand">IRON<br>RIDGE</div>
    <div class="caliber">9MM</div>
    <div class="load">115GR FMJ</div>
  </section>

  <section class="panel bottom-side">
    <div class="panel-inset" style="left:30px;top:22px;width:419px;height:55px;">
      <div class="brand-name brand-lockup"><span class="brand-mark"></span>IRON RIDGE ARMORY</div>
    </div>
  </section>

  <section class="panel end-flap end-left">
    <div class="panel-inset" style="left:30px;top:32px;width:58px;height:186px;">
      <div class="brand-name end-lockup">IRON RIDGE<br>ARMORY</div>
    </div>
  </section>

  <section class="panel end-flap end-right">
    <div class="panel-inset" style="left:22px;top:32px;width:58px;height:186px;">
      <div class="brand-name end-lockup">IRON RIDGE<br>ARMORY</div>
    </div>
  </section>

</main>
</body>
</html>
```